Steadfast Voyage Partners Capability Statement

Steadfast Voyage Partners is a Corporate Travel Management company based in Brisbane, Australia. Please review our 'About Us' page of our website to gain an understanding of our company culture (www.steadfastvoyagepartners.example.com.au). We are extremely customer focused. We see ourselves as an extension of our client's business.We require a powerful 1 page infographic that highlights what we do - 'Capability Statement' to use as an initial introduction to prospect clients when they ask for information about us.* Our Core Competencies - Service / People / Technology (this is our tagline so I think the document should follow this format)* A Company snapshot - Office location and website (needs to be editable to add Licence information)* Performance / Key Benefits (needs to editable to add in testimonials and case studies)* Client retention result 96%* Employee retention 98%* Affiliations & Partnerships (we will add)*Awards (see details to include)* Contact Details (at the bottom of the page - Marcus Van Heerden marcus@svpartners.example.com.au+61 448 187 226Differentiators (for us to complete so doc must be editable)The format of the document needs to be easily modified when required. I have attached the company logos and branding colours / font etc. Thank youRegardsMiriam

Target Market(s)

Medium businesses Australian based

Industry/Entity Type

Travel Industry

Font styles to use
Sans Serif

Colors
abd036

Requirements
Must have
• Content Outlined and corporate colours. Must be easily editable.

```html
<!DOCTYPE html>
<html lang="en">
<head>
<meta charset="utf-8">
<title>Steadfast Voyage Partners – Capability Statement</title>
<link href="https://fonts.googleapis.com/css2?family=Montserrat:ital,wght@0,400;0,500;0,600;0,700;1,600;1,700&display=swap" rel="stylesheet">
<style>
  :root {
    --green: #3cb64a;
    --lime: #abd036;
    --quote-green: #7cc242;
    --ink: #2e2e2e;
    --grey-text: #555;
    --footer-grey: #5f6062;
    --backdrop: #e7e7e7;
    --white: #ffffff;
    --rule: #cfcfcf;
  }
  * { box-sizing: border-box; margin: 0; padding: 0; }
  html, body { width: 684px; height: 1200px; overflow: hidden; }
  body {
    background: var(--backdrop);
    font-family: "Montserrat", Arial, sans-serif;
    color: var(--ink);
    position: relative;
  }
  .sheet {
    position: absolute; left: 0; top: 117px;
    width: 684px; height: 966px;
    background: var(--white);
    overflow: hidden;
  }

  /* Header */
  .masthead { position: absolute; left: 0; top: 0; width: 100%; height: 129px; }
  .brand { position: absolute; left: 40px; top: 30px; }
  .brand-name {
    display: flex; align-items: center; gap: 10px;
    font-size: 21px; font-weight: 600; color: var(--ink); letter-spacing: -0.3px;
  }
  .brand-mark { width: 16px; height: 16px; background: var(--lime); flex: none; }
  .brand-tagline {
    margin: 8px 0 0 26px;
    font-size: 11px; font-weight: 700; font-style: italic; color: var(--green); letter-spacing: 0.4px;
  }
  .brand-tagline span { color: var(--rule); font-style: normal; padding: 0 3px; }
  .masthead-divider { position: absolute; left: 408px; top: 16px; width: 1px; height: 100px; background: var(--rule); }
  .snapshot { position: absolute; left: 440px; top: 24px; font-size: 11px; color: var(--ink); line-height: 1.3; }
  .snapshot-row { display: flex; gap: 10px; margin-bottom: 10px; align-items: flex-start; }
  .snapshot-row svg { flex: none; margin-top: 1px; }
  .snapshot-web { color: var(--green); font-size: 14px; font-weight: 500; }
  .snapshot-abn { padding-left: 26px; }

  /* Hero */
  .hero { position: absolute; left: 0; top: 129px; width: 100%; height: 262px; overflow: hidden; }
  .hero-photo {
    position: absolute; left: 300px; top: 0; right: 0; bottom: 0;
    background: linear-gradient(180deg, #c9c3b6 0%, #e8e2d6 30%, #8a6a4a 62%, #3e2c1e 100%);
  }
  .hero-shape { position: absolute; left: 0; top: 0; }
  .hero-copy { position: absolute; left: 40px; top: 36px; color: var(--white); }
  .hero-title { font-size: 32px; font-weight: 400; line-height: 1.3; }
  .hero-sub { font-size: 20px; font-weight: 700; font-style: italic; margin-top: 8px; }
  .hero-line { font-size: 18px; font-weight: 400; line-height: 1.4; margin-top: 10px; }

  /* Benefits */
  .benefits { position: absolute; left: 40px; top: 410px; width: 605px; }
  .section-title { font-size: 15px; font-weight: 600; color: var(--green); }
  .benefits p { font-size: 10.6px; line-height: 1.35; color: var(--ink); margin-top: 10px; }

  /* Testimonials */
  .testimonials {
    position: absolute; left: 60px; top: 554px; width: 566px; height: 128px;
    background: var(--quote-green); border-radius: 18px; transform: skewX(-8deg);
  }
  .testimonial-list { transform: skewX(8deg); padding: 10px 36px 0 62px; color: var(--white); }
  .testimonial { position: relative; font-size: 10.4px; line-height: 1.3; margin-bottom: 18px; }
  .testimonial::before { content: "\201C"; position: absolute; left: -16px; top: -12px; font-size: 28px; font-weight: 700; }
  .testimonial-author { display: block; text-align: right; font-style: italic; font-weight: 700; font-size: 10px; margin-top: 4px; position: relative; }
  .testimonial-author::before { content: "\201D"; position: absolute; right: 60px; top: -8px; font-size: 26px; font-style: normal; }

  /* Stats */
  .stats {
    position: absolute; left: 0; top: 708px; width: 100%; height: 46px;
    background: var(--green); color: var(--white);
    display: flex; align-items: center; justify-content: space-around;
    font-size: 19px; font-weight: 500; padding: 0 12px;
  }

  /* Partners and awards */
  .partners { position: absolute; left: 40px; top: 776px; width: 240px; }
  .partners .section-title { font-size: 12.5px; color: var(--ink); display: inline-block; border-bottom: 2px solid var(--green); padding-bottom: 2px; }
  .partner-grid { display: grid; grid-template-columns: 1fr 1fr; row-gap: 16px; margin-top: 16px; font-size: 12px; font-weight: 600; color: var(--footer-grey); }
  .awards-divider { position: absolute; left: 576px; top: 0; }
  .awards { position: absolute; left: 610px; top: 780px; display: flex; gap: 26px; }
  .award-rule { position: absolute; left: 574px; top: 782px; width: 1px; height: 86px; background: var(--rule); }
  .award-badge { width: 58px; height: 76px; }

  /* Footer */
  .contact-bar {
    position: absolute; left: 0; top: 887px; width: 100%; height: 79px;
    background: var(--footer-grey); color: var(--white); font-size: 12px;
  }
  .contact-label { position: absolute; left: 40px; top: 8px; font-weight: 600; font-size: 12px; }
  .contact-name { position: absolute; left: 40px; top: 25px; color: var(--lime); font-weight: 600; font-size: 12.5px; border-bottom: 1px solid var(--lime); }
  .contact-row { position: absolute; left: 40px; right: 40px; top: 52px; display: flex; align-items: center; justify-content: space-between; }
  .contact-item { display: flex; align-items: center; gap: 7px; }
  .contact-sep { width: 1px; height: 22px; background: #888; }
</style>
</head>
<body>
<main class="sheet">

  <header class="masthead">
    <div class="brand">
      <div class="brand-name"><span class="brand-mark"></span>Steadfast Voyage Partners</div>
      <div class="brand-tagline">PEOPLE<span>|</span>SERVICE<span>|</span>TECHNOLOGY</div>
    </div>
    <div class="masthead-divider"></div>
    <div class="snapshot">
      <div class="snapshot-row">
        <svg width="14" height="16" viewBox="0 0 14 16"><path d="M7 1a5 5 0 0 0-5 5c0 4 5 9 5 9s5-5 5-9a5 5 0 0 0-5-5z" fill="none" stroke="#888" stroke-width="1.2"/><circle cx="7" cy="6" r="1.8" fill="#888"/></svg>
        <span>Ground Floor, 48 Harbour Street<br>Kelvin Grove QLD 4059</span>
      </div>
      <div class="snapshot-row">
        <svg width="14" height="14" viewBox="0 0 14 14"><circle cx="7" cy="7" r="6" fill="none" stroke="#888" stroke-width="1.2"/><path d="M1 7h12M7 1c-3 3-3 9 0 12M7 1c3 3 3 9 0 12" fill="none" stroke="#888" stroke-width="1"/></svg>
        <span class="snapshot-web">svpartners.example.com.au</span>
      </div>
      <div class="snapshot-abn">ABN 12 345 678 901</div>
    </div>
  </header>

  <section class="hero">
    <div class="hero-photo" role="img" aria-label="Photo of a passenger jet seen through airport terminal windows beside rows of lounge seating"></div>
    <svg class="hero-shape" width="684" height="262" viewBox="0 0 684 262" aria-hidden="true">
      <defs>
        <linearGradient id="heroShade" x1="0" y1="0" x2="0" y2="1">
          <stop offset="0" stop-color="#000" stop-opacity="0"/>
          <stop offset="0.45" stop-color="#000" stop-opacity="0.05"/>
          <stop offset="1" stop-color="#000" stop-opacity="0.75"/>
        </linearGradient>
      </defs>
      <path d="M0 0H320C380 50 400 200 360 262H0Z" fill="#3cb64a"/>
      <rect x="0" y="0" width="684" height="262" fill="url(#heroShade)"/>
    </svg>
    <div class="hero-copy">
      <h1 class="hero-title">Dynamic Multi<br>Award Winning</h1>
      <p class="hero-sub">team of industry experts</p>
      <p class="hero-line">that deliver confidence and<br>business travel certainty.</p>
    </div>
  </section>

  <section class="benefits">
    <h2 class="section-title">Performance / Key Benefits</h2>
    <p>Lorem ipsum dolor sit amet, consectetur adipiscing elit, sed do eiusmod tempor incididunt ut labore et dolore magna aliqua. Ut enim ad minim veniam, quis nostrud exercitation ullamco laboris nisi ut aliquip ex ea commodo consequat.</p>
    <p>Duis aute irure dolor in reprehenderit in voluptate velit esse cillum dolore eu fugiat nulla pariatur. Excepteur sint occaecat cupidatat non proident, sunt in culpa qui officia deserunt mollit anim id est laborum."</p>
  </section>

  <section class="testimonials">
    <div class="testimonial-list">
      <blockquote class="testimonial">Lorem ipsum dolor sit amet, consectetur adipiscing elit, sed do eiusmod tempor incididunt ut labore et dolore magna aliqua.<cite class="testimonial-author">- John Doe</cite></blockquote>
      <blockquote class="testimonial">Lorem ipsum dolor sit amet, consectetur adipiscing elit, sed do eiusmod tempor incididunt ut labore et dolore magna aliqua.<cite class="testimonial-author">- John Doe</cite></blockquote>
    </div>
  </section>

  <section class="stats">
    <span>* Client retention result 96%</span>
    <span>* Employee retention 98%</span>
  </section>

  <section class="partners">
    <h2 class="section-title">Affiliations &amp; Partnerships</h2>
    <div class="partner-grid">
      <span>Voyagelink</span><span>Farebridge</span>
      <span>Wanderhub</span><span>The Skyline Lounge</span>
    </div>
  </section>
  <div class="award-rule"></div>
  <div class="awards" aria-label="Industry awards">
    <svg class="award-badge" viewBox="0 0 58 76" role="img" aria-label="Award badge"><rect x="4" y="4" width="50" height="68" rx="4" fill="#e9f3d8" stroke="#abd036"/></svg>
    <svg class="award-badge" viewBox="0 0 58 76" role="img" aria-label="Award badge"><rect x="4" y="4" width="50" height="68" rx="4" fill="#e9f3d8" stroke="#abd036"/></svg>
    <svg class="award-badge" viewBox="0 0 58 76" role="img" aria-label="Award badge"><circle cx="29" cy="38" r="28" fill="#eeeeee" stroke="#bdbdbd"/></svg>
  </div>

  <footer class="contact-bar">
    <div class="contact-label">Contact</div>
    <div class="contact-name">Marcus Van Heerden</div>
    <div class="contact-row">
      <span class="contact-item">
        <svg width="12" height="9" viewBox="0 0 12 9"><rect x="0.5" y="0.5" width="11" height="8" fill="none" stroke="#abd036"/><path d="M0.5 0.5 6 5l5.5-4.5" fill="none" stroke="#abd036"/></svg>
        marcus@svpartners.example.com.au
      </span>
      <span class="contact-sep"></span>
      <span class="contact-item">
        <svg width="11" height="11" viewBox="0 0 11 11"><path d="M2 1l2 2-1 1.5c.8 1.5 2 2.7 3.5 3.5L8 7l2 2-1.5 1.5C4.5 10 1 6.5.5 2.5Z" fill="#abd036"/></svg>
        +61 455 903 618
      </span>
      <span class="contact-sep"></span>
      <span class="contact-item">
        <svg width="11" height="11" viewBox="0 0 14 14"><circle cx="7" cy="7" r="6" fill="none" stroke="#abd036" stroke-width="1.4"/><path d="M1 7h12M7 1c-3 3-3 9 0 12M7 1c3 3 3 9 0 12" fill="none" stroke="#abd036"/></svg>
        svpartners.example.com.au
      </span>
    </div>
  </footer>

</main>
</body>
</html>
```